TLB Shark card

This is a serious business card for a retired attorney with a sarcastic sense of humor. Incorporate into the design: shark with the tag line, Harmless unless provoked. The image could be graphic but not comic. The card should have a classic, sophisticated, professional look. Partial to minimalist, even Asian designs. Color options are black/ white (though this can easily go too cartoonish), gray tones, blue gray tones, blue. Open to something unexpected, even color, as long as the look is professional. The shark image attached is what we've been using but it isn't a design requirement.(Not sure why entire image isn't visible.)
Updates

No company Howard L Brisbane Name should be more prominent than the tag

This is the first time I've done this, so I apologize for not posting all this info up front. Some of it was in the narrative but to make it easier, I'm listing all the info that should be on the card. Howard L Brisbane Attorney at Law shark image Harmless unless provoked 27815 Velvet Harbor Street Dana Point, CA 92631 555-814-2073 hbrisbane@quellmail.net There is no company. The tag, Harmless unless provoked, should be less prominent than the name.

Industry/Entity Type

Attorney

Contact Information for Business Card

27815 Velvet Harbor Street
Dana Point, CA 92631
555-814-2073
hbrisbane@quellmail.net

```html
<!DOCTYPE html>
<html lang="en">
<head>
<meta charset="utf-8">
<title>TLB Shark Card</title>
<link href="https://fonts.googleapis.com/css2?family=Jost:wght@400;500&display=swap" rel="stylesheet">
<style>
  :root {
    --page: #fafafa;
    --card: #0a0b0c;
    --band-top: #06263b;
    --band-bottom: #041722;
    --shark-tone: #11506a;
    --shark-fade: rgba(17, 80, 106, 0);
    --ink: #ffffff;
    --rule: #cfeff5;
  }
  * { margin: 0; padding: 0; box-sizing: border-box; }
  html, body {
    width: 1200px;
    height: 666px;
    overflow: hidden;
    background: var(--page);
  }
  .business-card {
    position: absolute;
    left: 50px;
    top: 31px;
    width: 1103px;
    height: 607px;
    background: var(--card);
    overflow: hidden;
    font-family: "Jost", "Futura", sans-serif;
    color: var(--ink);
  }
  .ocean-band {
    position: absolute;
    inset: 0;
    width: 1103px;
    height: 607px;
  }
  .shark-artwork {
    position: absolute;
    left: 165px;
    top: 158px;
    width: 755px;
    height: 300px;
    border-radius: 45% 55% 40% 60% / 50% 50% 50% 50%;
    background: radial-gradient(ellipse at 55% 48%, var(--shark-tone) 0%, rgba(17, 80, 106, 0.75) 40%, var(--shark-fade) 75%);
  }
  .identity {
    position: absolute;
    left: 0;
    width: 100%;
    top: 244px;
    text-align: center;
  }
  .identity__name {
    font-size: 61px;
    font-weight: 500;
    letter-spacing: 1px;
    line-height: 68px;
  }
  .identity__rule {
    display: block;
    width: 550px;
    height: 1.5px;
    margin: 3px auto 0;
    background: linear-gradient(90deg, rgba(207, 239, 245, 0.2), var(--rule) 20%, var(--rule) 80%, rgba(207, 239, 245, 0.2));
  }
  .identity__tagline {
    font-size: 31px;
    font-weight: 500;
    letter-spacing: 0.5px;
    line-height: 40px;
    margin-top: 1px;
  }
  .contact {
    position: absolute;
    left: 0;
    width: 100%;
    top: 492px;
    text-align: center;
    font-size: 26px;
    font-weight: 500;
    letter-spacing: 0.3px;
  }
  .contact__row {
    display: flex;
    justify-content: center;
    align-items: center;
    gap: 6px;
    line-height: 34px;
  }
  .contact__phone { margin-left: 16px; }
  .contact__icon { width: 16px; height: 22px; fill: var(--ink); }
  .contact__icon--phone { width: 28px; height: 20px; }
  .contact__rule {
    display: block;
    width: 952px;
    height: 1px;
    margin: 3px auto 6px;
    background: linear-gradient(90deg, rgba(255,255,255,0.15), rgba(255,255,255,0.85) 15%, rgba(255,255,255,0.85) 85%, rgba(255,255,255,0.15));
  }
</style>
</head>
<body>
  <main class="business-card">
    <svg class="ocean-band" viewBox="0 0 1103 607" aria-hidden="true">
      <defs>
        <linearGradient id="band-fill" x1="0" y1="0" x2="0" y2="1">
          <stop offset="0" stop-color="#06263b"/>
          <stop offset="1" stop-color="#041722"/>
        </linearGradient>
      </defs>
      <path d="M0,195 Q551,92 1103,195 L1103,420 Q551,530 0,420 Z" fill="url(#band-fill)"/>
    </svg>

    <div class="shark-artwork" role="img" aria-label="Stylised teal shark outline swimming behind the name and tagline"></div>

    <header class="identity">
      <h1 class="identity__name">Howard L Brisbane</h1>
      <span class="identity__rule"></span>
      <p class="identity__tagline">Harmless unless provoked</p>
    </header>

    <footer class="contact">
      <div class="contact__row">
        <svg class="contact__icon" viewBox="0 0 18 24" aria-hidden="true">
          <path d="M9 1C4.6 1 2 4.2 2 8c0 5 7 15 7 15s7-10 7-15c0-3.8-2.6-7-7-7zm0 10a3 3 0 1 1 0-6 3 3 0 0 1 0 6z"/>
        </svg>
        <span class="contact__address">27815 Velvet Harbor Street Dana Point, CA 92631</span>
        <svg class="contact__icon contact__icon--phone contact__phone" viewBox="0 0 28 20" aria-hidden="true">
          <path d="M14 2C7 2 2 4 1 7l1 3 5-1 1-3c2-1 10-1 12 0l1 3 5 1 1-3C26 4 21 2 14 2z"/>
          <path d="M8 10h12l4 8H4z"/>
          <circle cx="14" cy="14" r="2.4" fill="#0a0b0c"/>
        </svg>
        <span>555-814-2073</span>
      </div>
      <span class="contact__rule"></span>
      <div class="contact__row">
        <svg class="contact__icon" viewBox="0 0 20 20" aria-hidden="true">
          <path d="M8.5 11.5l3-3" stroke="#ffffff" stroke-width="2" fill="none" stroke-linecap="round"/>
          <path d="M10 5l2-2a3.5 3.5 0 0 1 5 5l-2 2M10 15l-2 2a3.5 3.5 0 0 1-5-5l2-2" stroke="#ffffff" stroke-width="2.2" fill="none" stroke-linecap="round"/>
        </svg>
        <span>hbrisbane@quellmail.net</span>
      </div>
    </footer>
  </main>
</body>
</html>
```